Readable, Vibrant Large Shop Front Poster for Tutoring School.

Uncluttered design for the windows of our Business.
It needs to be readable from a distance.
It will be split across two windows. I've uploaded a picture of the premises. The poster is unfortunately split in two- see the shopfront photo - It will be in the two Square windows where the balloons are now.
I've also uploaded our logo which will be used as signage/ on the roof and would like the posters to tie in with it.

What we want to stand out
Over all :
That we are a Tutoring School Specializing in Secondary/VCE Studies

On the left hand side:
- 1 hour lessons are $20 with no joining fees or contracts (casual week to week bookings)

The right hand side:
-Weekly Lessons no contracts
-Summer School
-Holiday Program
-Workshops
-VCE EXAM PREP

Need B0 size (1000mm x 1414mm)

Requirements
Must have
• It must have large clear writing.
Nice to have
• a border top and bottom of the logo swirls, We don't need the business name on this poster.
Should not have
• Not a fan of Purple or Lime Green.

```html
<!DOCTYPE html>
<html lang="en">
<head>
<meta charset="utf-8">
<title>Learning Point – Window Poster</title>
<link rel="stylesheet" href="https://fonts.googleapis.com/css2?family=Arimo:wght@700&display=swap">
<style>
  :root {
    --navy-deep: #12064f;
    --band-blue: #3a4c9f;
    --wave-top-dark: #1b2d7e;
    --wave-top-light: #66abd5;
    --wave-bottom-dark: #0a6db2;
    --wave-bottom-light: #b6d7ea;
    --text-blue: #233f8f;
    --bullet-teal: #1e6f9f;
    --paper: #ffffff;
    --mark-teal: #4db6c6;
  }
  html, body {
    margin: 0;
    padding: 0;
    overflow: hidden;
    background: var(--paper);
  }
  .poster {
    position: relative;
    width: 849px;
    height: 1200px;
    overflow: hidden;
    background: var(--paper);
    font-family: "Arimo", Arial, sans-serif;
  }
  .poster__backdrop {
    position: absolute;
    inset: 0;
    width: 849px;
    height: 1200px;
  }
  .offer-list {
    position: absolute;
    left: 0;
    top: 0;
    margin: 0;
    padding: 0;
    list-style: none;
  }
  .offer-list__item {
    position: absolute;
    left: 222px;
    color: var(--text-blue);
    font-weight: 700;
    font-size: 47px;
    line-height: 53px;
    white-space: nowrap;
    letter-spacing: 0.2px;
  }
  .offer-list__item::before {
    content: "";
    position: absolute;
    left: -43px;
    top: 22px;
    width: 11px;
    height: 11px;
    background: var(--bullet-teal);
  }
  .offer-list__item--weekly   { top: 248px; }
  .offer-list__item--summer   { top: 397px; }
  .offer-list__item--holiday  { top: 493px; left: 218px; }
  .offer-list__item--workshop { top: 587px; }
  .offer-list__item--vce      { top: 684px; }
  .brand-bar__name {
    position: absolute;
    left: 256px;
    top: 1087px;
    width: 560px;
    margin: 0;
    color: var(--paper);
    font-weight: 700;
    font-size: 54px;
    line-height: 62px;
    letter-spacing: 4px;
    text-align: center;
    white-space: nowrap;
  }
</style>
</head>
<body>
  <main class="poster">
    <svg class="poster__backdrop" viewBox="0 0 1624 2297" preserveAspectRatio="none" aria-hidden="true">
      <defs>
        <linearGradient id="wave-top-fill" x1="0" y1="0" x2="0" y2="940" gradientUnits="userSpaceOnUse">
          <stop offset="0" stop-color="var(--wave-top-dark)" style="stop-color:#1b2d7e"/>
          <stop offset="1" stop-color="var(--wave-top-light)" style="stop-color:#66abd5"/>
        </linearGradient>
        <linearGradient id="wave-bottom-fill" x1="0" y1="1025" x2="0" y2="1960" gradientUnits="userSpaceOnUse">
          <stop offset="0" style="stop-color:#0a6db2"/>
          <stop offset="0.55" style="stop-color:#5fa6d2"/>
          <stop offset="1" style="stop-color:#b6d7ea"/>
        </linearGradient>
      </defs>
      <path class="wave wave--top" fill="url(#wave-top-fill)"
        d="M0,0 H1624 V40 C1560,120 1450,180 1280,180 C1100,180 920,105 720,110
           C570,115 495,175 470,265 C445,355 385,395 250,395 C150,395 105,405 110,450
           C118,520 170,585 190,655 C210,725 190,800 140,855 C95,905 35,930 0,940 Z"/>
      <path class="wave wave--bottom" fill="url(#wave-bottom-fill)"
        d="M1624,1030 C1500,1018 1442,1080 1440,1200 C1438,1300 1450,1400 1446,1500
           C1442,1590 1400,1640 1300,1660 C1150,1690 1000,1640 800,1600
           C600,1560 440,1530 330,1590 C255,1635 220,1700 180,1760
           C125,1845 60,1920 0,1960 H1624 Z"/>
      <rect class="brand-bar" x="0" y="1960" width="1624" height="337" style="fill:#3a4c9f"/>
      <rect class="brand-bar__stripe" x="0" y="2060" width="1624" height="170" style="fill:#12064f"/>
      <rect class="brand-bar__block" x="0" y="1978" width="412" height="319" style="fill:#12064f"/>
      <circle class="brand-bar__dot" cx="225" cy="2137" r="105" style="fill:#4db6c6"/>
    </svg>

    <ul class="offer-list">
      <li class="offer-list__item offer-list__item--weekly">WEEKLY LESSONS NO<br>CONTRACTS</li>
      <li class="offer-list__item offer-list__item--summer">SUMMER SCHOOL</li>
      <li class="offer-list__item offer-list__item--holiday">HOLIDAY PROGRAM</li>
      <li class="offer-list__item offer-list__item--workshop">WORKSHOPS</li>
      <li class="offer-list__item offer-list__item--vce">VCE EXAM PREP</li>
    </ul>

    <p class="brand-bar__name">LEARNING POINT</p>
  </main>
</body>
</html>
```